Need Stunning Website for Talent Acquisition (Recruiting) Agency

Hello, I am seeking a very professional, high-quality website that reflects our Talent Acquisition agency, Kindred Hires. Our agency slogan is "Talent Acquisition. Differently." We are in fact different - we are a full service agency that provides services most others do not, and our website needs to immediately reflect that something is different about us when they visit our site.

This contest is to do complete website design and coding, including all graphics, features, plugins, and design elements. The graphics are very important on the site and must be of the highest professional quality. One critical aspect is that the imagery must convey that we serve clients in a variety of industries, including business, healthcare, churches and religious organizations, non-profits, manufacturing, retail, and more. We recruit for both professional level positions (e.g. CEO, COO, Pastor), as well as entry level (e.g. secretary, caregiver, factory worker).
The following pages should be designed:
Home Page - a captivating home page that immediately tells our brand story, what makes us different, and the value that we bring to the table.
Client Services Page - a page that talks more about the services we provide and why we produce better results. This page will cover the 5 C's in greater detail as well as all the things that make us different.
Industries - The industries we serve
Request Services - a page where clients can submit details about a job they would like us to recruit for, including attaching a job description if they have one
Candidates Page - a simple page that encourages prospective candidates to submit their resume for review
About Us - Common about us page
Blog - Common blog page
Contact Us - a contact page for general inquiries
The website must be built in an ultra-SEO friendly manner and optimized for speed and performance. As mentioned above, you will be responsible for providing all graphics for the site (copyright compliant).
The website will need to be compatible with Elementor Pro (I have subscription) and Yoast SEO. It needs to be designed on a high-quality wordpress theme that receives regular updates. It also needs instant chat messaging feature. Would like a traditional menu bar at the top of the page (not a fan of menu's that are hidden or put on the side of the page).

Please, please, please - - do NOT waste my time with generic/stock templates, low-quality graphics, etc. We are a PREMIUM agency and our website needs to reflect that.

In the future we will add a job board - I do not want that initially - but will want the option to add it later.

Must also have the ability to upload documents /attachments on the contact page/form.

It probably goes without saying, but the page must be fully responsive - suitable to work on all device types.

Target Market(s)

Businesses

Industry/Entity Type

Talent Acquisition (Recruiting) Agency

Coding

Coded - Design and coding required

Number of Pages Required

5+ page

Requirements
Must have
• Please see brief
Should not have
• No generic template/stock website or graphics - must have PREMIUM feel.

```html
<!DOCTYPE html>
<html lang="en">
<head>
<meta charset="utf-8">
<title>Kindred Hires — Talent Acquisition. Differently.</title>
<link href="https://fonts.googleapis.com/css2?family=Poppins:ital,wght@0,400;0,500;0,600;0,700;0,800;1,400;1,500;1,700;1,800&display=swap" rel="stylesheet">
<style>
:root{
  --navy:#1c2354;
  --orange:#fdab0b;
  --orange-text:#f8a51a;
  --ink:#1a1a2e;
  --muted:#b9bdd6;
  --line:#d9dbe3;
  --white:#ffffff;
}
*{margin:0;padding:0;box-sizing:border-box}
html,body{width:1200px;height:3485px;overflow:hidden}
body{font-family:'Poppins',sans-serif;color:var(--ink);background:var(--white);position:relative}
.abs{position:absolute}
.section-title{position:absolute;left:0;width:1200px;text-align:center;font-style:italic;font-weight:800;color:var(--orange-text);font-size:46px;line-height:1}
.btn{position:absolute;display:flex;align-items:center;justify-content:center;border-radius:20px;font-weight:600;font-size:14px}
.btn-solid{background:var(--orange);color:var(--navy)}
.btn-outline{border:2px solid var(--orange);color:var(--orange-text);background:transparent}
.btn-light{border:2px solid var(--white);color:var(--white)}

/* header */
.site-header{top:0;left:0;width:1200px;height:87px;background:var(--navy)}
.brand-panel{top:0;left:0;width:440px;height:87px;background:var(--white);clip-path:polygon(0 0,390px 0,440px 87px,0 87px)}
.brand-name{font-weight:800;font-size:40px;color:var(--navy);letter-spacing:-1px;line-height:1;white-space:nowrap}
.brand-panel .brand-name{position:absolute;left:88px;top:22px}
.nav a{position:absolute;top:35px;font-size:14px;font-weight:500;color:var(--white);text-decoration:none}
.nav a.active{color:var(--orange)}
.nav-indicator{left:460px;top:0;width:64px;height:3px;background:var(--orange)}
.nav-indicator.bottom{top:84px}
.lang{left:1046px;top:31px;width:66px;height:26px;border:2px solid var(--orange);border-radius:13px;color:var(--orange);font-size:10px;font-weight:600;display:flex;align-items:center;justify-content:center;gap:10px}

/* hero */
.hero{top:87px;left:0;width:1200px;height:567px;background:linear-gradient(100deg,#5b6473 0%,#8a919a 35%,#6d7580 60%,#3f4652 100%)}
.hero::after{content:"";position:absolute;inset:0;background:rgba(20,25,45,.35)}
.hero-copy{position:absolute;left:0;top:160px;width:1200px;text-align:center;z-index:1}
.hero-title{font-style:italic;font-weight:800;font-size:46px;line-height:56px}
.hero-title .o{color:var(--orange)}
.hero-title .w{color:var(--white)}
.hero-sub{color:var(--white);font-style:italic;font-weight:500;font-size:18px;line-height:26px;margin-top:14px}
.hero .btn{z-index:1}
.dots{position:absolute;top:519px;left:566px;display:flex;gap:10px;z-index:1}
.dots span{width:15px;height:15px;border:2px solid var(--white);border-radius:50%}
.dots span.on{border-color:var(--orange);background:radial-gradient(var(--orange) 35%,transparent 40%)}

/* why */
.why{top:654px;left:0;width:1200px;height:503px;background:var(--white);overflow:hidden}
.bubble{position:absolute;border-radius:50%;background:#fff6e6}
.why-media{left:88px;top:79px;width:496px;height:342px;background:linear-gradient(135deg,#4a5280,#7b83a8 55%,#59608a);display:flex;align-items:center;justify-content:center}
.why-media .brand-name{font-size:58px}
.why-copy{left:615px;top:118px;width:480px}
.why-copy h2{font-style:italic;font-weight:800;font-size:36px;line-height:44px;color:var(--orange-text);margin-left:3px}
.why-copy p{font-size:13.5px;line-height:22px;color:#333;margin-top:14px}
.why-copy ul{list-style:none;margin-top:10px}
.why-copy li{font-size:12.5px;font-weight:500;line-height:26.5px;padding-left:12px;position:relative;white-space:nowrap}
.why-copy li::before{content:"";position:absolute;left:0;top:9px;border-left:5px solid var(--orange);border-top:4px solid transparent;border-bottom:4px solid transparent}
.why-copy .about-btn{position:static;width:128px;height:36px;margin-top:26px}

/* services */
.services{top:1157px;left:0;width:1200px;height:464px;background:var(--navy)}
.service{position:absolute;top:150px;width:220px;color:var(--white)}
.service-icon{width:74px;height:74px;border-radius:50%;background:var(--orange);display:flex;align-items:center;justify-content:center}
.service h3{font-size:19px;font-weight:600;line-height:24px;margin-top:21px}
.service p{font-size:12px;line-height:18px;color:var(--muted);margin-top:6px}
.circle-arrow{position:absolute;width:36px;height:36px;border:2px solid var(--orange);border-radius:50%;display:flex;align-items:center;justify-content:center}

/* industries */
.industries{top:1621px;left:0;width:1200px;height:576px;background:#fbfbfc}
.industry{position:absolute;width:234px;height:124px;border:2px solid var(--line);background:var(--white);display:flex;flex-direction:column;align-items:center;justify-content:center;gap:14px;font-size:16px;font-weight:500}

/* audiences */
.audiences{top:2197px;left:0;width:1200px;height:303px;background:linear-gradient(90deg,#27306a,#333c78 50%,#27306a)}
.audience{position:absolute;top:68px;width:440px;text-align:center;color:var(--white)}
.audience h2{font-size:31px;font-weight:600}
.audience p{font-size:14px;line-height:22px;margin-top:12px}
.divider-v{left:599px;top:40px;width:1px;height:225px;background:rgba(255,255,255,.35)}

/* blogs */
.blogs{top:2500px;left:0;width:1200px;height:566px;background:var(--white)}
.post{position:absolute;top:160px;width:309px;height:240px;border-radius:0 0 40px 0;overflow:hidden;color:var(--white)}
.post-date{position:absolute;left:15px;top:15px;font-size:12px;font-style:italic;display:flex;align-items:center;gap:6px}
.post-title{position:absolute;left:15px;bottom:14px;right:20px;font-size:14px;line-height:21px;font-weight:500}

/* footer */
.site-footer{top:3066px;left:0;width:1200px;height:379px;background:var(--navy)}
.site-footer .brand-name{position:absolute;left:88px;top:44px;color:var(--white);font-size:38px}
.footer-head{font-style:italic;font-weight:700;font-size:19px;color:var(--orange-text)}
.contact-row{position:absolute;left:88px;display:flex;align-items:center;gap:18px;color:var(--white);font-size:14px}
.contact-ico{width:36px;height:36px;background:rgba(255,255,255,.08);display:flex;align-items:center;justify-content:center}
.quick a{display:block;color:var(--white);font-size:14px;line-height:26.5px;text-decoration:none}
.quick a.active{color:var(--orange);text-decoration:underline}
.field{position:absolute;background:rgba(255,255,255,.14);display:flex;align-items:center;gap:10px;padding-left:12px;color:var(--white);font-size:11px}
.to-top{left:1119px;top:3374px;width:52px;height:52px;border-radius:50%;background:var(--orange);display:flex;align-items:center;justify-content:center}

.copyright{top:3445px;left:0;width:1200px;height:40px;background:var(--orange)}
.copyright p{position:absolute;left:88px;top:12px;font-size:13px;color:var(--navy)}
.social{position:absolute;top:10px;width:20px;height:20px;border:1.5px solid var(--navy);border-radius:3px}
</style>
</head>
<body>

<header class="abs site-header">
  <div class="abs brand-panel">
    <div class="brand-name">Kindred Hires</div>
  </div>
  <nav class="nav">
    <div class="abs nav-indicator"></div>
    <div class="abs nav-indicator bottom"></div>
    <a class="active" style="left:472px">Home</a>
    <a style="left:549px">About Us</a>
    <a style="left:644px">Our Services</a>
    <a style="left:767px">Industries</a>
    <a style="left:871px">Blogs</a>
    <a style="left:946px">Contact Us</a>
  </nav>
  <div class="abs lang">EN <svg width="8" height="5" viewBox="0 0 8 5"><path d="M0 0h8L4 5z" fill="#fdab0b"/></svg></div>
</header>

<section class="abs hero" role="img" aria-label="Team meeting in a bright office with colleagues around a table">
  <div class="hero-copy">
    <div class="hero-title"><span class="o">Talent Acquisition.</span><br><span class="w">Differently.</span></div>
    <div class="hero-sub">We recruit both Professional Level Positions,<br>as well as Entry Level</div>
  </div>
  <div class="btn btn-solid" style="left:466px;top:361px;width:268px;height:34px">Schedule a Free Consultation</div>
  <div class="dots"><span></span><span class="on"></span><span></span></div>
</section>

<section class="abs why">
  <div class="bubble" style="left:700px;top:60px;width:130px;height:130px"></div>
  <div class="bubble" style="left:530px;top:290px;width:130px;height:130px"></div>
  <div class="bubble" style="left:880px;top:290px;width:100px;height:100px"></div>
  <div class="bubble" style="left:1145px;top:400px;width:90px;height:90px"></div>
  <div class="bubble" style="left:40px;top:50px;width:70px;height:70px"></div>
  <div class="bubble" style="left:1080px;top:65px;width:64px;height:64px"></div>
  <div class="abs why-media" role="img" aria-label="Business team meeting photo with brand name overlay">
    <div class="brand-name">Kindred Hires</div>
  </div>
  <div class="abs why-copy">
    <h2>Why Choose Us</h2>
    <p>Lorem Ipsum is simply dummy text of the printing and typesetting<br>industry. Lorem Ipsum has been the industry’s...</p>
    <ul>
      <li>Lorem ipsum dolor sit amet, consectetur adipiscing elit.</li>
      <li>Vivamus ac orci at magna aliquet sagittis id quis libero.</li>
      <li>Aenean eu est finibus, vehicula elit ut, tincidunt tortor.</li>
    </ul>
    <div class="btn btn-outline about-btn">About Us</div>
  </div>
</section>

<section class="abs services">
  <div class="section-title" style="top:73px">Our Services</div>
  <div class="service" style="left:88px">
    <div class="service-icon"><svg width="38" height="38" viewBox="0 0 38 38" fill="none" stroke="#1c2354" stroke-width="2.5"><circle cx="19" cy="19" r="16"/><circle cx="19" cy="15" r="6"/><path d="M9 30c3-6 17-6 20 0"/></svg></div>
    <h3>Correct hiring.</h3>
    <p>Lorem Ipsum is simply dummy text of the printing and typesetting...</p>
  </div>
  <div class="service" style="left:350px">
    <div class="service-icon"><svg width="36" height="36" viewBox="0 0 36 36" fill="none" stroke="#1c2354" stroke-width="2.5"><rect x="12" y="4" width="18" height="24" rx="2"/><path d="M4 30h16l6-6M4 24h8"/><circle cx="21" cy="14" r="4"/></svg></div>
    <h3>Compensate fairly.</h3>
    <p>Lorem Ipsum is simply dummy text of the printing and typesetting...</p>
  </div>
  <div class="service" style="left:612px">
    <div class="service-icon"><svg width="40" height="40" viewBox="0 0 40 40" fill="none" stroke="#1c2354" stroke-width="2.2"><circle cx="20" cy="20" r="8"/><circle cx="10" cy="10" r="6"/><circle cx="30" cy="10" r="6"/><circle cx="10" cy="30" r="6"/><circle cx="30" cy="30" r="6"/></svg></div>
    <h3>Currencies of choice.</h3>
    <p>Lorem Ipsum is simply dummy text of the printing and typesetting...</p>
  </div>
  <div class="service" style="left:874px">
    <div class="service-icon"><svg width="38" height="38" viewBox="0 0 38 38" fill="none" stroke="#1c2354" stroke-width="2.5"><path d="M6 16h6l14-8v22l-14-8H6z"/><path d="M10 22l3 9h4l-2-9M30 12l4-3M31 19h5M30 26l4 3"/></svg></div>
    <h3>Communicate with FOCUS.</h3>
    <p>Lorem Ipsum is simply dummy text of the printing and typesetting...</p>
  </div>
  <div class="circle-arrow" style="left:459px;top:348px"><svg width="14" height="10" viewBox="0 0 14 10" fill="none" stroke="#fdab0b" stroke-width="1.8"><path d="M13 5H1M5 1L1 5l4 4"/></svg></div>
  <div class="btn btn-solid" style="left:507px;top:348px;width:185px;height:36px">View All Services</div>
  <div class="circle-arrow" style="left:704px;top:348px"><svg width="14" height="10" viewBox="0 0 14 10" fill="none" stroke="#fdab0b" stroke-width="1.8"><path d="M1 5h12M9 1l4 4-4 4"/></svg></div>
</section>

<section class="abs industries">
  <div class="section-title" style="top:75px">Industries</div>
  <div class="industry" style="left:233px;top:152px"><svg width="38" height="36" viewBox="0 0 38 36" fill="none" stroke="#f8a51a" stroke-width="2"><path d="M3 34V16l8-5v5l8-5v5l8-5v23zM29 34V4h6v30M8 24h4M16 24h4"/></svg>Industries</div>
  <div class="industry" style="left:483px;top:152px"><svg width="38" height="34" viewBox="0 0 38 34" fill="none" stroke="#f8a51a" stroke-width="2"><path d="M19 31S3 21 3 11a8 8 0 0116-3 8 8 0 0116 3c0 10-16 20-16 20z"/><path d="M7 17h8l3-5 4 9 3-4h6"/></svg>Healthcare</div>
  <div class="industry" style="left:733px;top:152px"><svg width="36" height="38" viewBox="0 0 36 38" fill="none" stroke="#f8a51a" stroke-width="2"><path d="M18 2v8M14 6h8M8 20l10-10 10 10v16H8zM2 36V26l6-4M34 36V26l-6-4M15 36v-8h6v8"/></svg>Churches</div>
  <div class="industry" style="left:233px;top:292px"><svg width="36" height="38" viewBox="0 0 36 38" fill="none" stroke="#f8a51a" stroke-width="2"><path d="M18 2l15 9v16l-15 9-15-9V11z"/><text x="18" y="23" font-size="9" font-family="Poppins,sans-serif" font-weight="700" fill="#f8a51a" stroke="none" text-anchor="middle">NFT</text></svg>Non-Profits</div>
  <div class="industry" style="left:483px;top:292px"><svg width="40" height="38" viewBox="0 0 40 38" fill="none" stroke="#f8a51a" stroke-width="2"><path d="M3 36V18l9-6v6l9-6v24zM21 36V8l8-5 8 5v28M8 26h4M26 14h6M26 22h6M26 30h6"/></svg>Manufacturing</div>
  <div class="industry" style="left:733px;top:292px"><svg width="40" height="36" viewBox="0 0 40 36" fill="none" stroke="#f8a51a" stroke-width="2"><path d="M4 4h32l3 9H1zM1 13c0 4 8 4 8 0 0 4 8 4 8 0 0 4 6 4 6 0 0 4 8 4 8 0 0 4 8 4 8 0M4 18v16h32V18M10 34v-9h8v9M23 24h8v6h-8z"/></svg>Retail</div>
  <div class="btn btn-solid" style="left:530px;top:460px;width:140px;height:34px">View More</div>
</section>

<section class="abs audiences" role="img" aria-label="Blue-tinted photo of professionals at work">
  <div class="abs divider-v"></div>
  <div class="audience" style="left:147px">
    <h2>Employers</h2>
    <p>Lorem Ipsum is simply dummy text of the printing<br>and typesetting industry. Lorem Ipsum...</p>
  </div>
  <div class="btn btn-light" style="left:294px;top:186px;width:142px;height:34px">Read More</div>
  <div class="audience" style="left:620px">
    <h2>Candidates</h2>
    <p>Lorem Ipsum is simply dummy text of the printing<br>and typesetting industry. Lorem Ipsum...</p>
  </div>
  <div class="btn btn-solid" style="left:766px;top:186px;width:142px;height:34px">Read More</div>
</section>

<section class="abs blogs">
  <div class="section-title" style="top:82px">Blogs</div>
  <article class="post" style="left:113px;background:linear-gradient(160deg,#8d96a6,#4b5466)" role="img" aria-label="Two professionals shaking hands in an office">
    <div class="post-date"><svg width="13" height="13" viewBox="0 0 13 13" fill="none" stroke="#fdab0b" stroke-width="1.6"><rect x="1" y="2" width="11" height="10"/><path d="M1 5h11M4 0v3M9 0v3"/></svg>25 June, 2022</div>
    <div class="post-title">Lorem Ipsum is simply dummy text of the printing and typesetting...</div>
  </article>
  <article class="post" style="left:445px;background:linear-gradient(160deg,#6f87a8,#37507a)" role="img" aria-label="Smiling team gathered at a desk">
    <div class="post-date"><svg width="13" height="13" viewBox="0 0 13 13" fill="none" stroke="#fdab0b" stroke-width="1.6"><rect x="1" y="2" width="11" height="10"/><path d="M1 5h11M4 0v3M9 0v3"/></svg>25 June, 2022</div>
    <div class="post-title" style="bottom:34px">Lorem Ipsum is simply dummy text of the printing and typesetting...</div>
  </article>
  <div class="abs" style="left:461px;top:386px;width:34px;height:34px;border-radius:50%;background:var(--orange);display:flex;align-items:center;justify-content:center"><svg width="14" height="10" viewBox="0 0 14 10" fill="none" stroke="#1c2354" stroke-width="1.8"><path d="M1 5h12M9 1l4 4-4 4"/></svg></div>
  <article class="post" style="left:778px;background:linear-gradient(160deg,#b6bcc6,#6c7482)" role="img" aria-label="Colleagues reviewing work together">
    <div class="post-date"><svg width="13" height="13" viewBox="0 0 13 13" fill="none" stroke="#fdab0b" stroke-width="1.6"><rect x="1" y="2" width="11" height="10"/><path d="M1 5h11M4 0v3M9 0v3"/></svg>25 June, 2022</div>
    <div class="post-title">Lorem Ipsum is simply dummy text of the printing and typesetting...</div>
  </article>
  <div class="btn btn-outline" style="left:538px;top:451px;width:125px;height:35px">View All</div>
</section>

<footer class="abs site-footer">
  <div class="brand-name">Kindred Hires</div>
  <div class="abs footer-head" style="left:88px;top:140px">Conatct Info</div>
  <div class="contact-row" style="top:187px"><div class="contact-ico"><svg width="14" height="18" viewBox="0 0 14 18" fill="#fdab0b"><path d="M7 0a7 7 0 00-7 7c0 5 7 11 7 11s7-6 7-11a7 7 0 00-7-7zm0 10a3 3 0 110-6 3 3 0 010 6z"/></svg></div>Lorbach, Canton Nord</div>
  <div class="contact-row" style="top:245px"><div class="contact-ico"><svg width="16" height="16" viewBox="0 0 16 16" fill="#fdab0b"><path d="M3 1l3 3-2 2c1 2 3 4 5 5l2-2 3 3-2 3C7 15 1 9 1 3z"/></svg></div><span style="color:var(--orange);text-decoration:underline">+41 (0)70 555 0182</span></div>
  <div class="contact-row" style="top:299px"><div class="contact-ico"><svg width="16" height="12" viewBox="0 0 16 12" fill="#fdab0b"><path d="M0 0h16v12H0z"/><path d="M0 0l8 7 8-7" fill="none" stroke="#1c2354" stroke-width="1.5"/></svg></div>info@kindredhires.com</div>
  <div class="abs footer-head" style="left:351px;top:140px">Quick Links</div>
  <div class="abs quick" style="left:351px;top:178px">
    <a class="active">Home</a><a>About Us</a><a>Our Services</a><a>Industries</a><a>Blogs</a><a>Contact Us</a>
  </div>
  <div class="abs" style="left:502px;top:84px;width:1px;height:235px;background:rgba(255,255,255,.2)"></div>
  <div class="abs footer-head" style="left:543px;top:80px;font-size:25px">Inquire Now!</div>
  <div class="abs" style="left:543px;top:116px;font-size:11px;color:var(--muted)">We guarantee a returned phone call within 24 business hours.</div>
  <div class="field" style="left:543px;top:142px;width:275px;height:38px"><svg width="12" height="12" viewBox="0 0 12 12" fill="none" stroke="#fdab0b" stroke-width="1.4"><circle cx="6" cy="4" r="3"/><path d="M1 12c1-4 9-4 10 0"/></svg>Name</div>
  <div class="field" style="left:543px;top:192px;width:275px;height:38px"><svg width="13" height="10" viewBox="0 0 13 10" fill="none" stroke="#fdab0b" stroke-width="1.4"><rect x="1" y="1" width="11" height="8"/><path d="M1 1l5.5 4L12 1"/></svg>Email</div>
  <div class="field" style="left:543px;top:242px;width:275px;height:38px"><svg width="9" height="13" viewBox="0 0 9 13" fill="none" stroke="#fdab0b" stroke-width="1.4"><rect x="1" y="1" width="7" height="11" rx="1"/></svg>Phone</div>
  <div class="field" style="left:835px;top:142px;width:276px;height:138px;align-items:flex-start;padding-top:12px"><svg width="12" height="12" viewBox="0 0 12 12" fill="none" stroke="#fdab0b" stroke-width="1.4"><path d="M1 1h10v7H5l-3 3V8H1z"/></svg>Message</div>
  <div class="btn btn-light" style="left:543px;top:300px;width:113px;height:35px">Submit</div>
</footer>
<div class="abs to-top"><svg width="20" height="22" viewBox="0 0 20 22" fill="none" stroke="#fff" stroke-width="2"><path d="M2 1h16M10 21V6M4 12l6-6 6 6"/></svg></div>

<div class="abs copyright">
  <p>© Copyright 2022 <u>Kindred Hires</u>. All Rights Reserved.</p>
  <div class="social" style="left:1001px"></div>
  <div class="social" style="left:1031px"></div>
  <div class="social" style="left:1061px;background:var(--navy)"></div>
  <div class="social" style="left:1091px"></div>
</div>

</body>
</html>
```